Landing Page for Social Media Optimization

We need a Landing page made for Social Media Optimization we are going to be calling this Trevinoxa an entire package that is for small to large businesses. We will manage all aspects of social media from Plimvera, Quondel Marskove, Zubrath+ for a monthly fee helping them reach customers.

We simply need a web page that shows "The Package" and with a form that lets the user fill in there contact details so we can get in touch. The contact details we'd like to collect are

Name
Email
Company
Telephone

```html
<!DOCTYPE html>
<html lang="en">
<head>
<meta charset="utf-8">
<title>Trevinoxa — Social Media Optimization</title>
<link rel="stylesheet" href="https://fonts.googleapis.com/css2?family=Fjalla+One&family=Raleway:wght@300;400&display=swap">
<style>
  :root {
    --green: #7bb540;
    --green-text: #86c14a;
    --orange: #e2702b;
    --orange-line: #c95d1e;
    --brown: #654c27;
    --brown-text: #5a4320;
    --paper: #f3f3ef;
    --teal: #6bb3c2;
    --dark: #323232;
    --footer: #bcbcbc;
    --white: #ffffff;
    --field-text: #444444;
  }
  * { box-sizing: border-box; margin: 0; padding: 0; }
  html, body { width: 1200px; height: 2230px; overflow: hidden; }
  body { position: relative; background: var(--paper); font-family: Arial, Helvetica, sans-serif; }

  .hero { position: absolute; left: 0; top: 0; width: 1200px; height: 758px; }
  .hero-photo {
    position: absolute; inset: 0;
    background:
      radial-gradient(ellipse 260px 380px at 720px 470px, #4d5f7e 0%, rgba(77,95,126,0) 100%),
      radial-gradient(ellipse 300px 420px at 960px 430px, #2a2a2e 0%, rgba(42,42,46,0) 100%),
      linear-gradient(100deg, #e9b774 0%, #d9a56a 22%, #b08a66 40%, #c9c4bd 60%, #a9b8c6 80%, #7f95a8 100%);
  }
  .site-header {
    position: absolute; left: 0; top: 15px; width: 1200px; height: 127px;
    background: var(--green); color: var(--white);
    display: flex; align-items: center; justify-content: space-between; padding: 0 45px 0 44px;
  }
  .brand { font-family: 'Fjalla One', sans-serif; font-size: 64px; letter-spacing: 1px; line-height: 1; }
  .tagline { font-family: 'Raleway', sans-serif; font-weight: 300; font-size: 31px; line-height: 37px; text-align: right; }

  .hero-copy { position: absolute; left: 33px; top: 318px; font-family: 'Fjalla One', sans-serif; color: var(--white); text-transform: uppercase; white-space: nowrap; }
  .hero-copy .line-a { font-size: 41px; line-height: 56px; }
  .hero-copy .line-b { font-size: 52px; line-height: 60px; }
  .hero-copy .line-c { font-size: 32px; line-height: 48px; color: var(--green-text); }

  .order-button {
    position: absolute; display: flex; align-items: center; gap: 22px;
    background: var(--orange); color: var(--white);
    font-family: 'Raleway', sans-serif; font-weight: 300; font-size: 31px; letter-spacing: -0.5px;
    white-space: nowrap; overflow: hidden;
    padding-left: 26px; height: 60px;
  }
  .order-button svg { width: 38px; height: 38px; flex: none; }
  .hero .order-button { left: 32px; top: 492px; width: 426px; }

  .services { position: absolute; left: 0; top: 758px; width: 1200px; height: 502px; }
  .service { position: absolute; top: 84px; width: 250px; }
  .service-icon { width: 200px; height: 200px; border-radius: 50%; background: var(--brown); margin: 0 auto; }
  .service h3 { font-family: 'Fjalla One', sans-serif; font-weight: 400; font-size: 27px; color: var(--brown-text); text-align: center; margin-top: 12px; line-height: 40px; text-transform: uppercase; white-space: nowrap; }
  .service p { font-size: 17px; line-height: 20px; color: var(--brown-text); margin-top: 8px; }
  .service-1 { left: 22px; } .service-2 { left: 326px; } .service-3 { left: 628px; } .service-4 { left: 934px; }

  .welcome { position: absolute; left: 0; top: 1260px; width: 1200px; height: 341px; background: var(--teal); color: var(--white); text-align: center; }
  .welcome h2 { font-family: 'Raleway', sans-serif; font-weight: 300; font-size: 56px; margin-top: 44px; line-height: 64px; }
  .welcome p { width: 1050px; margin: 22px auto 0; font-size: 17px; line-height: 22px; }
  .social-row { display: flex; justify-content: center; gap: 26px; margin-top: 34px; }
  .social-item { display: flex; align-items: center; gap: 8px; font-family: 'Raleway', sans-serif; font-size: 18px; }
  .social-item .dot { width: 52px; height: 52px; border-radius: 50%; background: var(--white); }

  .package { position: absolute; left: 114px; top: 1696px; width: 356px; }
  .package-head { height: 61px; background: var(--dark); color: var(--white); display: flex; align-items: center; gap: 22px; padding-left: 27px; font-family: 'Raleway', sans-serif; font-weight: 300; font-size: 34px; text-transform: uppercase; }
  .package-head svg { width: 38px; height: 38px; }
  .package-list { list-style: none; background: var(--orange); }
  .package-list li { height: 61px; display: flex; align-items: center; padding-left: 23px; color: var(--white); font-size: 17px; border-bottom: 1px solid var(--orange-line); white-space: nowrap; }
  .package-list li:last-child { border-bottom: none; }

  .order-form { position: absolute; left: 630px; top: 1690px; width: 430px; }
  .order-form h2 { font-family: 'Raleway', sans-serif; font-weight: 300; font-size: 36px; color: var(--dark); letter-spacing: -1.5px; line-height: 54px; white-space: nowrap; }
  .field { display: block; width: 427px; height: 48px; margin-top: 13px; background: var(--white); border: none; padding-left: 21px; font-family: Arial, Helvetica, sans-serif; font-size: 17px; color: var(--field-text); }
  .order-form h2 + .field { margin-top: 23px; }
  .order-form .order-button { position: relative; width: 428px; margin-top: 23px; }

  .site-footer { position: absolute; left: 0; top: 2158px; width: 1200px; height: 72px; background: var(--footer); color: var(--white); display: flex; align-items: center; justify-content: space-between; padding: 0 30px; font-size: 16px; }
  .footer-social { display: flex; gap: 12px; }
  .footer-social .social-item { font-size: 14px; gap: 5px; }
  .footer-social .dot { width: 26px; height: 26px; border-radius: 50%; background: var(--white); }
</style>
</head>
<body>
  <section class="hero">
    <div class="hero-photo" role="img" aria-label="Photo of a young couple sitting outdoors, working together on a laptop"></div>
    <header class="site-header">
      <div class="brand">TREVINOXA</div>
      <div class="tagline">The most trusted company in<br>Social Media Optimization</div>
    </header>
    <div class="hero-copy">
      <div class="line-a">Manage all aspects of</div>
      <div class="line-b">Social media from</div>
      <div class="line-c">Plimvera, Quondel, Marskove, Zubrath+</div>
    </div>
    <a class="order-button">
      <svg viewBox="0 0 38 38"><circle cx="19" cy="19" r="19" fill="#fff"/><path d="M10 19h15M19 12l7 7-7 7" stroke="#e2702b" stroke-width="4" fill="none" stroke-linecap="square"/></svg>
      order the package now!
    </a>
  </section>

  <section class="services">
    <div class="service service-1">
      <div class="service-icon" role="img" aria-label="Icon of a connected globe above a group of people"></div>
      <h3>Media Marketing</h3>
      <p>Lorem ipsum dolor sit amet, consectetuer adipiscing elit, sed diam nonummy nibh euismod tincidunt ut laoreet .</p>
    </div>
    <div class="service service-2">
      <div class="service-icon" role="img" aria-label="Icon of a presenter at a chart board before an audience"></div>
      <h3>Market Planning</h3>
      <p>Duis autem vel eum iriure dolor in hendrerit in vulputate velit ess molestie consequat, vel illum dolore eu feugiat nulla .</p>
    </div>
    <div class="service service-3">
      <div class="service-icon" role="img" aria-label="Icon of a figure beside rising arrows"></div>
      <h3>Strategic Growth</h3>
      <p>Nam liber tempor cum soluta nobis eleifend option congue nihil imperdiet doming id quod mazim placerat facer.</p>
    </div>
    <div class="service service-4">
      <div class="service-icon" role="img" aria-label="Icon of a figure pushing an upward curved arrow"></div>
      <h3>Content Strategy</h3>
      <p>Nam liber tempor cum soluta nobis eleifend option congue nihil imperdiet doming id quod mazim placerat facer.</p>
    </div>
  </section>

  <section class="welcome">
    <h2>Welcome to Trevinoxa</h2>
    <p>Claritas est etiam processus dynamicus, qui sequitur mutationem consuetudium lectorum. Mirum est notare quam littera gothica, quam nunc putamus parum claram, anteposuerit litterarum formas humanitatis per seacula quarta decima et quinta decima. Eodem modo typi, qui nunc nobis videntur parum clari, fiant sollemnes in futurum.</p>
    <div class="social-row">
      <span class="social-item"><span class="dot"></span>Quondel</span>
      <span class="social-item"><span class="dot"></span>Plimvera</span>
      <span class="social-item"><span class="dot"></span>Zubrath+</span>
      <span class="social-item"><span class="dot"></span>Fennoral</span>
      <span class="social-item"><span class="dot"></span>Marskove</span>
    </div>
  </section>

  <aside class="package">
    <div class="package-head">
      <svg viewBox="0 0 38 38"><circle cx="19" cy="19" r="19" fill="#fff"/><path d="M10 19h15M19 12l7 7-7 7" stroke="#323232" stroke-width="4" fill="none" stroke-linecap="square"/></svg>
      The Package
    </div>
    <ul class="package-list">
      <li>Dolor sit amet, consectetuer adipiscing elit</li>
      <li>Ut wisi enim ad minim veniam, quis</li>
      <li>Duis autem vel eum iriure dolor in hendrer</li>
      <li>Typi non habent claritatem insitam est</li>
      <li>Claritas est etiam processus dynamicus</li>
    </ul>
  </aside>

  <form class="order-form">
    <h2>Fill up to order The Package</h2>
    <input class="field" type="text" placeholder="Name">
    <input class="field" type="email" placeholder="Email">
    <input class="field" type="text" placeholder="Company">
    <input class="field" type="tel" placeholder="Telephone">
    <a class="order-button">
      <svg viewBox="0 0 38 38"><circle cx="19" cy="19" r="19" fill="#fff"/><path d="M10 19h15M19 12l7 7-7 7" stroke="#e2702b" stroke-width="4" fill="none" stroke-linecap="square"/></svg>
      order the package now!
    </a>
  </form>

  <footer class="site-footer">
    <div>Trevinoxa © 2014 All Rights Reserved &nbsp;|&nbsp; Privacy Policy</div>
    <div class="footer-social">
      <span class="social-item"><span class="dot"></span>Quondel</span>
      <span class="social-item"><span class="dot"></span>Plimvera</span>
      <span class="social-item"><span class="dot"></span>Zubrath+</span>
      <span class="social-item"><span class="dot"></span>Marskove</span>
    </div>
  </footer>
</body>
</html>
```